Flyer für einen Pflegedienst
Die Kommunikation ist herausragend, es wird sofort in absolut unglaublich schneller Zeit auf Wünsche reagiert. Die Ergebnisse sind perfekt auf die eigenen Wünsche zugeschnitten und passen zum Corporate Design. Die Dateien sind alle samt fehlerfrei, in bester Qualität und können ohne Umwege an die Druckerei gegeben werden. Auch kurzfristige Änderungen nach Fertigstellung wurden sofort durchgeführt. Höflich, respektvoll, zuvorkommend. Mein 1 zu 1 Designer
Zielgruppe
Wir sind ein Pflegedienst, unsere Zielgruppe sind alle Menschen die Unterstützung brauchen. Das sind im Hauptteil Senioren.
Aufgabenstellung
Der Flyer soll im DIN A5 Format designed sein. Der Print soll hochwertig sein. Wir möchten vor allem wohlhabendere Kunden damit ansprechen. Er soll die Kunden direkt packen, aber auch nicht zu viele Informationen beinhalten, die einen überfordern.

```html
<!DOCTYPE html>
<html lang="de">
<head>
<meta charset="utf-8">
<title>Pflege Lindhof – Flyer</title>
<link href="https://fonts.googleapis.com/css2?family=Source+Sans+3:ital,wght@0,300;0,400;0,600;0,700;1,400;1,600&display=swap" rel="stylesheet">
<style>
:root{
  --stage:#393e41;
  --paper:#ececec;
  --green:#087d2f;
  --green-soft:#3f9a2c;
  --lime:#95c11f;
  --red:#c20f22;
  --ink:#3c3c3c;
  --white:#ffffff;
}
*{box-sizing:border-box;margin:0;padding:0}
html,body{width:1200px;height:1200px;overflow:hidden;background:var(--stage);font-family:"Source Sans 3",Arial,sans-serif;color:var(--ink)}
.flyer{position:absolute;top:242px;width:537px;height:762px;background:var(--paper);overflow:hidden;box-shadow:0 14px 18px rgba(0,0,0,.35)}
.flyer--front{left:31px}
.flyer--back{left:623px}
.shape-layer{position:absolute;inset:0;width:537px;height:762px}
.photo{position:absolute;inset:0}
.abs{position:absolute}
.call-tab{position:absolute;background:var(--red);color:var(--white);display:flex;align-items:center;gap:9px;font-weight:600;font-size:13px;letter-spacing:.1px}
.call-tab .dot{width:22px;height:22px;border-radius:50%;border:2.5px solid var(--green-soft);background:var(--white)}
.front-call{left:222px;top:0;width:315px;height:45px;border-bottom-left-radius:12px;padding-left:26px}
.back-call{left:217px;top:277px;width:271px;height:41px;border-top-left-radius:12px;padding-left:12px;font-size:12px}
.brand{position:absolute;left:22px;top:18px;text-align:center;width:170px}
.brand-mark{width:46px;height:46px;border-radius:50%;border:3px solid var(--green);margin:0 auto 8px}
.brand-name{font-size:29px;font-weight:600;color:var(--green);line-height:1}
.brand-tag{font-size:10.5px;color:#555;margin-top:6px}
.intro{right:15px;top:61px;width:230px;text-align:right;font-size:12.6px;line-height:15.6px;font-weight:300;color:#444}
.intro b,.lead b{font-weight:700}
.quote{background:rgba(236,236,236,.55);color:#2d2d2d;font-style:italic;font-weight:600}
.front-quote{left:20px;top:382px;width:260px;height:132px;padding:14px 18px 0 31px;font-size:16px;line-height:20.3px}
.qm{font-weight:700;font-style:normal;font-size:20px;line-height:1}
.badge{left:224px;top:542px;width:94px;height:94px;border-radius:50%;background:var(--white);box-shadow:3px 4px 0 #0a5e25}
.services-title{left:20px;top:650px;color:var(--white);font-weight:600;font-size:17px;text-decoration:underline;text-underline-offset:4px}
.services{color:var(--white);font-size:13.4px;line-height:15px;list-style:none}
.services li{position:relative;padding-left:11px;margin-bottom:9px}
.services li::before{content:"";position:absolute;left:0;top:5px;width:6px;height:6px;background:var(--lime)}
.services--a{left:206px;top:657px;width:130px}
.services--b{left:345px;top:657px;width:190px}
.band{position:absolute;left:0;bottom:0;width:100%;height:14px;background:var(--lime)}
.headline{left:232px;top:25px;color:var(--white);font-size:17.5px;font-weight:300;line-height:22px}
.headline .name{color:var(--lime);font-weight:600;font-size:21px}
.headline u{text-underline-offset:3px}
.back-para{left:233px;top:84px;width:290px;color:var(--white);font-size:13.4px;line-height:16.8px;font-weight:300}
.back-para b{font-weight:700}
.lead{left:225px;top:208px;width:275px;font-size:14.6px;line-height:18.6px;font-weight:300;color:#444}
.back-quote{left:246px;top:474px;width:253px;height:94px;padding:14px 14px 0 18px;font-size:22.5px;line-height:28px;text-align:right}
.footer-mark{left:33px;top:670px;width:64px;height:64px;border-radius:50%;border:3px solid var(--green)}
.company{left:125px;top:680px;font-size:13.6px;line-height:16.5px;color:#444}
.company b{font-weight:700}
.contact{left:323px;top:680px;font-size:13.6px;line-height:16.5px;color:#444}
.contact li{list-style:none;display:flex;align-items:center;gap:5px}
.contact svg{width:11px;height:11px;flex:none}
.contact .tel{font-weight:700}
</style>
</head>
<body>

<section class="flyer flyer--front">
  <svg class="shape-layer" viewBox="0 0 537 762" aria-hidden="true">
    <path d="M0 168 L301 140 L537 168 L537 517 C430 575 330 601 270 601 C170 601 80 570 0 526 Z" fill="#8a7a55"/>
    <path d="M0 526 C80 570 170 601 270 601 C330 601 430 575 537 517 L537 762 L0 762 Z" fill="var(--green)"/>
  </svg>
  <div class="photo" role="img" aria-label="Foto: Pflegerin schiebt eine Seniorin im Rollstuhl, daneben ein älterer Herr mit Gehstock im Garten vor einem Backsteinhaus" style="clip-path:polygon(0 168px,301px 140px,537px 168px,537px 517px,270px 601px,0 526px);background:linear-gradient(180deg,#8b4a3a 0%,#6f7a4e 45%,#9bb065 75%,#7fa34a 100%)"></div>

  <div class="call-tab front-call"><span class="dot"></span>Kostenlose Beratung 0208 - 555 017 20</div>

  <div class="brand">
    <div class="brand-mark"></div>
    <div class="brand-name">Pflege Lindhof</div>
    <div class="brand-tag">Gemeinsam Leben, liebevoll Pflegen</div>
  </div>

  <p class="abs intro">Pflege Lindhof – Ihr <b>zuverlässiger Pflegedienst</b> für Mülheim an der Ruhr, Süd-Duisburg, Süd- &amp; West-Essen, Süd-Oberhausen, Ratingen &amp; Lintorf.</p>

  <blockquote class="abs quote front-quote"><span class="qm" style="position:absolute;left:11px;top:8px">«</span>Bei uns werden Sie liebevoll umsorgt und finden ein geborgenes Zuhause in einem Umfeld voller Herzlichkeit und Fürsorge. <span class="qm">»</span></blockquote>

  <div class="abs badge"></div>

  <h2 class="abs services-title">Unsere Leistungen:</h2>
  <ul class="abs services services--a">
    <li>Grundpflege</li>
    <li>Behandlungspflege</li>
    <li>Professionelle Wundversorgung</li>
  </ul>
  <ul class="abs services services--b">
    <li>Betreuung &amp; Hauswirtschaft</li>
    <li>Pflegeberatung nach §37.1</li>
    <li>Palliative Rundumversorgung</li>
  </ul>
  <div class="band"></div>
</section>

<section class="flyer flyer--back">
  <svg class="shape-layer" viewBox="0 0 537 762" aria-hidden="true">
    <path d="M0 0 H537 V202 L268 169 L0 202 Z" fill="var(--green)"/>
    <circle cx="107" cy="50" r="21" fill="var(--green-soft)"/>
  </svg>
  <div class="photo" role="img" aria-label="Foto: lächelnde Pflegerin misst einer Seniorin im Wohnzimmer den Blutdruck" style="clip-path:polygon(0 318px,537px 318px,537px 607px,268px 653px,0 607px);background:linear-gradient(90deg,#c9ad86 0%,#a78b62 40%,#3b8f86 65%,#e6d8c6 100%)"></div>

  <p class="abs headline">Jetzt mit <span class="name">Pflege Lindhof</span><br><u>mehr Lebensqualität sichern :</u></p>
  <p class="abs back-para">Von <b>qualifizierter medizinischer</b> Versorgung bis hin zu Seniorenbetreuung – bei uns steht das <b>Wohlbefinden und die Zufriedenheit</b> unserer Patienten an erster Stelle.</p>

  <p class="abs lead">Ein Anruf oder eine Nachricht genügt – <b>kontaktieren Sie</b> uns und entdecken Sie <b>unsere vielfältigen Pflegeleistungen.</b></p>
  <div class="call-tab back-call"><span class="dot"></span>Kostenlose Beratung 0208 - 555 017 20</div>

  <blockquote class="abs quote back-quote"><span class="qm">«</span> Gemeinsam leben, liebevoll pflegen <span class="qm">»</span></blockquote>

  <div class="abs footer-mark"></div>
  <address class="abs company" style="font-style:normal"><b>Pflege Lindhof</b><br>Ahornweg 7b<br>45470 Mülheim an der Ruhr</address>
  <ul class="abs contact">
    <li class="tel"><svg viewBox="0 0 12 12"><path d="M2.5 1 L4.5 1 L5.3 3.4 L4 4.4 C4.6 5.8 6.2 7.4 7.6 8 L8.6 6.7 L11 7.5 L11 9.5 C11 10.3 10.3 11 9.5 11 C5 11 1 7 1 2.5 C1 1.7 1.7 1 2.5 1 Z" fill="var(--green-soft)"/></svg>Tel. 0208 - 555 017 20</li>
    <li><svg viewBox="0 0 12 12"><rect x="1" y="2.5" width="10" height="7" fill="none" stroke="#555"/><path d="M1 2.5 L6 6.5 L11 2.5" fill="none" stroke="#555"/></svg>info@pflegelindhof.de</li>
    <li><svg viewBox="0 0 12 12"><circle cx="6" cy="6" r="4.8" fill="none" stroke="#555"/><ellipse cx="6" cy="6" rx="2" ry="4.8" fill="none" stroke="#555"/><path d="M1.2 6 H10.8" stroke="#555"/></svg>www.pflegelindhof.de</li>
  </ul>
  <div class="band"></div>
</section>

</body>
</html>
```